Brightfield Landscape Company flyer

I need a flyer to be mailed by the Kelvar parcel bureau for the open route bulk sender (orbs) program. I would two sides full color with one side dedicated to landscape construction and the other side dedicated to lawn maintenance. Services we offer for landscaping are: design, installation, drainage correction, grading, retaining walls, patios and water features. for the lawn maintenance:weekly lawn maintenance , lawn treatments, aerating / overseeding, mulch / pine needles and trimming shrubbery. The flyer has to state my contractor license number QTVR#7159. Thanks!

Target Market(s)

Homeowners with disposable incomes

Industry/Entity Type

Landscaping

Requirements
Must have
• logo, contractor seal and number. size should be 6"x12" and conform to the kpb standards for open route bulk sending.

```html
<!DOCTYPE html>
<html lang="en">
<head>
<meta charset="utf-8">
<title>Brightfield Landscape Company – Mailer</title>
<link href="https://fonts.googleapis.com/css2?family=Roboto+Condensed:ital,wght@0,400;0,700;1,700&family=Open+Sans:wght@400;600&family=Arimo:wght@700&display=swap" rel="stylesheet">
<style>
  :root{
    --green:#6cb33f;
    --green-dark:#4e8f2a;
    --ink:#1e1e1e;
    --grey:#6d6d6d;
    --paper:#ffffff;
    --bg:#e9e7e4;
    --lawn-top:#8fc95a;
    --lawn-bottom:#4f9a2a;
  }
  *{box-sizing:border-box;margin:0;padding:0}
  html,body{width:1200px;height:1189px;overflow:hidden;background:var(--bg)}
  body{position:relative;font-family:"Open Sans",sans-serif;color:var(--ink)}
  .card{position:absolute;width:960px;height:488px;background:var(--paper);overflow:hidden;box-shadow:0 2px 8px rgba(0,0,0,.18)}
  .card--front{left:110px;top:88px}
  .card--back{left:150px;top:616px}
  .abs{position:absolute}

  /* front */
  .hero-photo{left:0;top:0;width:960px;height:340px;
    background:linear-gradient(180deg,#5c6b4f 0%,#8a5060 22%,#4d7a2e 38%,var(--lawn-top) 55%,var(--lawn-bottom) 100%)}
  .logo-panel{background:var(--paper);clip-path:polygon(0 0,100% 0,94% 100%,0 100%);box-shadow:0 2px 4px rgba(0,0,0,.2)}
  .card--front .logo-panel{left:0;top:266px;width:322px;height:102px}
  .card--back .logo-panel{left:0;top:14px;width:326px;height:103px}
  .brand{display:flex;align-items:center;justify-content:center;gap:10px;height:100%;padding-right:20px}
  .brand__dot{width:22px;height:22px;border-radius:50%;background:var(--green)}
  .brand__name{font-family:"Roboto Condensed",sans-serif;font-weight:400;font-size:19px;color:#333;line-height:1.1;text-align:center}
  .tagline{left:0;top:368px;width:343px;height:30px;background:var(--green);clip-path:polygon(0 0,100% 0,94% 100%,0 100%);
    font-family:"Roboto Condensed",sans-serif;font-style:italic;font-weight:700;font-size:19px;color:#fff;padding:3px 0 0 18px}
  .license{font-family:"Open Sans",sans-serif;font-size:11px;color:var(--grey)}
  .card--front .license{left:316px;top:345px}
  .card--back .license{left:322px;top:72px}
  .thumb{border-radius:50%;border:4px solid #fff;box-shadow:0 0 0 4px var(--green),0 3px 6px rgba(0,0,0,.3)}
  .thumb--mower{left:467px;top:250px;width:138px;height:138px;background:radial-gradient(circle at 45% 50%,#a33 0 18%,#3a3a3a 19% 30%,#6eaa3d 31%)}
  .thumb--roots{left:635px;top:250px;width:138px;height:138px;background:linear-gradient(180deg,#9fd07a 0%,#6aa846 55%,#4a3426 62%,#3a271d 100%)}
  .thumb--mulch{left:804px;top:250px;width:138px;height:138px;background:radial-gradient(circle at 60% 40%,#e0a030 0 12%,#5b8a2c 13% 25%,#5a2a22 26%)}
  .cta{font-family:"Roboto Condensed",sans-serif;font-weight:700;font-size:16px;color:var(--ink)}
  .contact{font-family:"Open Sans",sans-serif;font-size:13.5px;line-height:20px;color:var(--ink)}
  .contact b{font-weight:600;margin-left:4px}
  .services{list-style:none;font-family:"Roboto Condensed",sans-serif;text-transform:uppercase}
  .services li{display:flex;align-items:center;gap:8px;white-space:nowrap}
  .leaf{width:11px;height:11px;background:var(--green);border-radius:0 70% 0 70%;flex:none}
  .card--front .services{font-size:15px;line-height:20.5px;color:var(--ink)}
  .card--front .services--a{left:480px;top:403px}
  .card--front .services--b{left:727px;top:403px}
  .footer-band{left:0;bottom:0;width:960px;height:14px;background:var(--green)}

  /* back */
  .service-panel{left:0;top:94px;width:590px;height:127px;background:var(--green)}
  .card--back .services{font-size:17.5px;line-height:23.5px;color:#fff}
  .card--back .leaf{background:#e6f3da}
  .card--back .services--a{left:24px;top:135px}
  .card--back .services--b{left:306px;top:135px}
  .seal{left:486px;top:31px;width:86px;height:86px;border-radius:50%;background:#fff;border:3px solid #3f6a45;box-shadow:inset 0 0 0 10px #e6ede2,inset 0 0 0 13px #3f6a45}
  .patio-photo{left:0;top:227px;width:590px;height:180px;
    background:linear-gradient(180deg,#6a4030 0%,#8a5a3c 30%,#d8d4cc 55%,#c9c4ba 75%,#5e9a36 100%)}
  .cta-band{left:0;top:388px;width:320px;height:39px;background:var(--green);clip-path:polygon(0 0,100% 0,96% 100%,0 100%);
    font-family:"Roboto Condensed",sans-serif;font-weight:700;font-size:18px;color:#fff;padding:8px 0 0 17px}
  .thumb--wall{left:370px;top:347px;width:96px;height:96px;background:linear-gradient(180deg,#7b9a52 0%,#9a6a4a 45%,#b88060 100%)}
  .thumb--fountain{left:484px;top:347px;width:96px;height:96px;background:radial-gradient(circle at 50% 45%,#c8a060 0 20%,#7a7060 21% 50%,#4d6a3a 51%)}
  .card--back .contact{left:17px;top:433px}
  .indicia{left:840px;top:17px;width:110px;height:90px;border:1px solid #000;font-family:"Arimo",sans-serif;font-weight:700;font-size:11.5px;line-height:14px;text-align:center;padding-top:10px}
  .address{left:716px;top:169px;width:225px;height:70px;border:1px solid #888;font-family:"Arimo",sans-serif;font-weight:700;font-size:12.5px;line-height:15px;padding:18px 0 0 22px}
</style>
</head>
<body>

<section class="card card--front" aria-label="Lawn maintenance side">
  <div class="abs hero-photo" role="img" aria-label="Photo of a manicured front lawn with flowering shrubs and a curved stone path"></div>
  <div class="abs logo-panel"><div class="brand"><span class="brand__dot"></span><span class="brand__name">Brightfield Landscape<br>Company</span></div></div>
  <div class="abs tagline">Landscape Design and Construction</div>
  <div class="abs license">license number QTVR#7159</div>
  <div class="abs thumb thumb--mower" role="img" aria-label="Photo of a lawn mower on grass"></div>
  <div class="abs thumb thumb--roots" role="img" aria-label="Photo of grass blades and roots in soil"></div>
  <div class="abs thumb thumb--mulch" role="img" aria-label="Photo of flowers in red mulch"></div>
  <div class="abs cta" style="left:25px;top:405px">CALL TODAY FOR YOUR FREE ESTIMATE!</div>
  <div class="abs contact" style="left:25px;top:429px">Your Name <b>000 0000</b><br>www.brightfieldlandscape.com</div>
  <ul class="abs services services--a">
    <li><span class="leaf"></span>Weekly Lawn Maintenance</li>
    <li><span class="leaf"></span>Lawn Treatments</li>
    <li><span class="leaf"></span>Aerating / Overseeding</li>
  </ul>
  <ul class="abs services services--b">
    <li><span class="leaf"></span>Mulch</li>
    <li><span class="leaf"></span>Pine Needles</li>
    <li><span class="leaf"></span>Trimming Shrubbery</li>
  </ul>
  <div class="abs footer-band"></div>
</section>

<section class="card card--back" aria-label="Landscape construction side">
  <div class="abs service-panel"></div>
  <div class="abs logo-panel"><div class="brand"><span class="brand__dot"></span><span class="brand__name">Brightfield Landscape<br>Company</span></div></div>
  <div class="abs license">license number QTVR#7159</div>
  <div class="abs seal" role="img" aria-label="Registered contractor seal"></div>
  <ul class="abs services services--a">
    <li><span class="leaf"></span>Design</li>
    <li><span class="leaf"></span>Installation</li>
    <li><span class="leaf"></span>Drainage Correction</li>
  </ul>
  <ul class="abs services services--b">
    <li><span class="leaf"></span>Grading</li>
    <li><span class="leaf"></span>Retaining Walls</li>
    <li><span class="leaf"></span>Patios and Water Features</li>
  </ul>
  <div class="abs patio-photo" role="img" aria-label="Photo of a stone patio with outdoor sofa beside a brick house"></div>
  <div class="abs cta-band">CALL TODAY FOR YOUR FREE ESTIMATE!</div>
  <div class="abs thumb thumb--wall" role="img" aria-label="Photo of a brick retaining wall with lamp"></div>
  <div class="abs thumb thumb--fountain" role="img" aria-label="Photo of a stone water fountain"></div>
  <div class="abs contact">Your Name <b>000 0000</b><br>www.brightfieldlandscape.com</div>
  <div class="abs indicia">PRSRT STD<br>ECRWSS<br>KPB POSTAGE<br>PAID<br>ORBS RETAIL</div>
  <div class="abs address">Local<br>Postal Customer</div>
</section>

</body>
</html>
```